Business Card for a Wedding Films Business

We require a business card design for our business 'Lewis Marrow Wedding Films'. The logo needs to look classy and high end.

Target Market(s)

Wedding Couples

Contact Information for Business Card

Lewis Marrow Wedding Films
07312 605 227
films@lewismarrowreels.com
www.lewismarrowreels.com

Facebook: @lewismarrowweddingfilms
Instagram: @lewismarrowfilms

Font styles to use
Sans Serif

Requirements
Must have
• Social media icons - Facebook and Instagram

```html
<!DOCTYPE html>
<html lang="en">
<head>
<meta charset="utf-8">
<title>Lewis Marrow Wedding Films – Business Card</title>
<link rel="stylesheet" href="https://fonts.googleapis.com/css2?family=Jost:wght@400;500&family=Quicksand:wght@500&display=swap">
<style>
  :root {
    --page: #d7d7d7;
    --card: #2e2f35;
    --card-glow: #41444c;
    --ink: #ffffff;
    --gold: #a08d55;
    --gold-light: #b8a767;
  }
  * { margin: 0; padding: 0; box-sizing: border-box; }
  html, body { width: 1200px; height: 800px; overflow: hidden; }
  body { background: var(--page); position: relative; font-family: "Jost", sans-serif; color: var(--ink); }

  .card {
    position: absolute;
    top: 284px;
    width: 430px;
    height: 239px;
    background: radial-gradient(ellipse 60% 70% at 35% 30%, var(--card-glow), var(--card) 75%);
    overflow: hidden;
  }
  .card--front { left: 110px; }
  .card--back { left: 638px; }

  .stripes { position: absolute; left: 0; top: 0; width: 430px; height: 239px; }
  .stripes .band-light { fill: var(--ink); }
  .stripes .band-gold { fill: var(--gold); }
  .card--back .stripes .band-gold { fill: var(--gold-light); }

  .wordmark { position: absolute; text-align: center; text-transform: uppercase; }
  .wordmark__name { font-weight: 500; font-size: 18px; letter-spacing: 4.2px; line-height: 1; }
  .wordmark__tag { font-weight: 500; font-size: 8.5px; letter-spacing: 5px; margin-top: 6px; line-height: 1; }
  .card--front .wordmark { left: 15px; top: 12px; }
  .card--back .wordmark { left: 160px; right: 0; top: 138px; }
  .card--back .wordmark__tag { font-size: 9px; letter-spacing: 5.4px; margin-top: 7px; }

  .brand-dot {
    position: absolute;
    left: 260px;
    top: 74px;
    width: 46px;
    height: 46px;
    border-radius: 50%;
    border: 2px solid var(--ink);
  }

  .person { position: absolute; left: 15px; top: 112px; }
  .person__bar { position: absolute; left: -15px; top: 0; width: 4px; height: 26px; background: var(--gold); }
  .person__name { font-weight: 500; font-size: 17px; letter-spacing: 2.6px; text-transform: uppercase; line-height: 1; }
  .person__role { font-family: "Quicksand", sans-serif; font-weight: 500; font-size: 11.5px; margin-top: 2px; }

  .contacts { position: absolute; left: 15px; list-style: none; font-family: "Quicksand", sans-serif; font-weight: 500; font-size: 12px; }
  .contacts--direct { top: 151px; }
  .contacts--social { top: 200px; }
  .contacts li { display: flex; align-items: center; height: 13.4px; }
  .contacts svg { width: 11px; height: 11px; margin-right: 5px; flex: none; }
  .social-square { width: 10px; height: 10px; background: var(--ink); border-radius: 2px; margin-right: 6px; flex: none; }
</style>
</head>
<body>

<section class="card card--front" aria-label="Business card front">
  <svg class="stripes" viewBox="0 0 430 239" aria-hidden="true">
    <polygon class="band-light" points="413,0 430,0 430,239 274,239"/>
    <polygon class="band-gold" points="428,0 440,0 301,239 289,239"/>
    <polygon class="band-gold" points="448,0 460,0 321,239 309,239"/>
    <polygon class="band-gold" points="468,0 480,0 341,239 329,239"/>
    <polygon class="band-gold" points="488,0 500,0 361,239 349,239"/>
    <polygon class="band-gold" points="508,0 520,0 381,239 369,239"/>
    <polygon class="band-gold" points="528,0 540,0 401,239 389,239"/>
    <polygon class="band-gold" points="548,0 560,0 421,239 409,239"/>
  </svg>

  <div class="wordmark">
    <div class="wordmark__name">Lewis Marrow</div>
    <div class="wordmark__tag">Wedding Films</div>
  </div>

  <div class="person">
    <span class="person__bar"></span>
    <div class="person__name">Lewis Marrow</div>
    <div class="person__role">CEO/ Owner</div>
  </div>

  <ul class="contacts contacts--direct">
    <li>
      <svg viewBox="0 0 12 12" fill="none" stroke="currentColor" stroke-width="1"><path d="M3 1.5 L4.6 3.6 L3.7 4.6 Q4.8 6.9 7.4 8.3 L8.4 7.4 L10.5 9 L9.4 10.5 Q5.5 10.3 2.2 6 Q1 3.9 1.6 2.5 Z"/><path d="M7 2.2 Q9.5 2.5 9.8 5"/></svg>
      07312 605 227
    </li>
    <li>
      <svg viewBox="0 0 12 12" fill="none" stroke="currentColor" stroke-width="1"><rect x="1" y="2.5" width="10" height="7"/><path d="M1 2.5 L6 6.5 L11 2.5"/></svg>
      films@lewismarrowreels.com
    </li>
    <li>
      <svg viewBox="0 0 12 12" fill="none" stroke="currentColor" stroke-width="1"><circle cx="6" cy="6" r="5"/><ellipse cx="6" cy="6" rx="2.2" ry="5"/><path d="M1 6 H11 M2 3.5 H10 M2 8.5 H10"/></svg>
      www.lewismarrowreels.com
    </li>
  </ul>

  <ul class="contacts contacts--social">
    <li><span class="social-square"></span>@lewismarrowweddingfilms</li>
    <li><span class="social-square"></span>@lewismarrowfilms</li>
  </ul>
</section>

<section class="card card--back" aria-label="Business card back">
  <svg class="stripes" viewBox="0 0 430 239" aria-hidden="true">
    <polygon class="band-gold" points="-12,0 0,0 141,239 129,239"/>
    <polygon class="band-gold" points="-34,0 -22,0 119,239 107,239"/>
    <polygon class="band-gold" points="-56,0 -44,0 97,239 85,239"/>
    <polygon class="band-gold" points="-78,0 -66,0 75,239 63,239"/>
    <polygon class="band-gold" points="-100,0 -88,0 53,239 41,239"/>
    <polygon class="band-gold" points="-122,0 -110,0 31,239 19,239"/>
  </svg>

  <span class="brand-dot"></span>
  <div class="wordmark">
    <div class="wordmark__name">Lewis Marrow</div>
    <div class="wordmark__tag">Wedding Films</div>
  </div>
</section>

</body>
</html>
```